Stationery design for pet company

We need a designer for stationery designs. The name of our company is Valtrix. We specialise in pet accessories as well as distribution of pet food. We also have a brand under us for our website called Brightwhiskerclub. We will need a letterhead for Valtrix and another for Brightwhiskerclub with matching envelopes. We also would like to have a business card design with name, contact details etc with the Valtrix logo on one side of the card. The other side of the business card should have the full logo of Brightwhiskerclub with our website www.brightwhiskerclub.com.

Target Market(s)

Stationery for Valtrix is for retail shops and suppliers, therefore should have a more professional feel. Stationery for Brightwhiskerclub is mainly for customers from the website.

Industry/Entity Type

Business

Requirements
Must have
• Preferably a use of black colour for the business card.
Nice to have
• Professional feel
Should not have
• Childish designs

```html
<!DOCTYPE html>
<html lang="en">
<head>
<meta charset="utf-8">
<title>Valtrix Stationery Set</title>
<link href="https://fonts.googleapis.com/css2?family=Open+Sans:wght@400;600;700&display=swap" rel="stylesheet">
<style>
  :root {
    --backdrop: #ababab;
    --margin: #ffffff;
    --paper: #ffffff;
    --card-black: #000000;
    --ink: #1a1a1a;
    --muted: #666666;
    --gold: #c9a04e;
    --gold-faint: #f4ecdc;
    --brand-purple: #8a4bb8;
    --placeholder-light: #e6e6e6;
    --placeholder-dark: #9a9a9a;
    --shadow: 0 1px 4px rgba(0,0,0,0.35);
  }
  * { box-sizing: border-box; margin: 0; padding: 0; }
  html, body { width: 1200px; height: 891px; overflow: hidden; background: var(--margin); }
  body { font-family: "Open Sans", Arial, sans-serif; color: var(--ink); position: relative; }
  .backdrop { position: absolute; left: 12px; top: 0; width: 1188px; height: 889px; background: var(--backdrop); }
  .piece { position: absolute; background: var(--paper); box-shadow: var(--shadow); overflow: hidden; }

  /* wordmark */
  .wordmark { display: flex; flex-direction: column; align-items: center; gap: 4px; }
  .wordmark-dot { border-radius: 50%; background: var(--gold); }
  .wordmark-name { font-weight: 700; color: var(--ink); letter-spacing: 0.12em; text-transform: uppercase; line-height: 1; }

  /* faint name decoration */
  .faint-name { position: absolute; font-weight: 700; color: var(--gold-faint); letter-spacing: 0.1em; text-transform: uppercase; line-height: 1; transform: translate(-50%, -50%); white-space: nowrap; }

  /* contact block */
  .contact { position: absolute; font-size: 8px; line-height: 1.45; color: #333; }
  .contact .label { color: var(--gold); }
  .gold-bar { position: absolute; background: var(--gold); }

  /* letterhead */
  .letterhead { left: 553px; top: 69px; width: 606px; height: 783px; }
  .letterhead .wordmark { position: absolute; left: 32px; top: 32px; width: 110px; }
  .letterhead .wordmark-dot { width: 36px; height: 36px; }
  .letterhead .wordmark-name { font-size: 17px; }
  .letterhead .contact { font-size: 8.6px; }

  /* envelope back */
  .envelope-back { left: 131px; top: 380px; width: 541px; height: 236px; }
  .flap { position: absolute; left: 0; top: 0; }
  .flap-name { position: absolute; left: 0; right: 0; top: 32px; text-align: center; font-size: 11px; font-weight: 600; color: var(--brand-purple); }
  .flap-web { position: absolute; left: 0; right: 0; top: 52px; text-align: center; font-size: 6.5px; color: #fff; letter-spacing: 0.1em; }

  /* envelope front */
  .envelope-front { left: 35px; top: 482px; width: 544px; height: 237px; }
  .envelope-front .wordmark { position: absolute; left: 20px; top: 20px; width: 84px; }
  .envelope-front .wordmark-dot { width: 28px; height: 28px; }
  .envelope-front .wordmark-name { font-size: 13px; }

  /* business card front */
  .card-black { left: 250px; top: 65px; width: 249px; height: 142px; border-radius: 11px; background: var(--card-black); }
  .mascot-area { position: absolute; left: 98px; top: 28px; width: 53px; height: 56px; border-radius: 6px;
    background: linear-gradient(180deg, var(--placeholder-light), var(--placeholder-dark)); }
  .club-name { position: absolute; left: 0; right: 0; top: 90px; text-align: center; font-size: 17px; font-weight: 600; color: var(--brand-purple); }
  .club-web { position: absolute; left: 0; right: 0; top: 118px; text-align: center; font-size: 8.5px; color: #fff; letter-spacing: 0.12em; }

  /* business card back */
  .card-white { left: 250px; top: 222px; width: 249px; height: 142px; border-radius: 11px; }
  .card-white .wordmark { position: absolute; left: 26px; top: 48px; width: 72px; }
  .card-white .wordmark-dot { width: 22px; height: 22px; }
  .card-white .wordmark-name { font-size: 11px; }
  .person { position: absolute; right: 18px; top: 24px; text-align: right; }
  .person-name { font-size: 8.5px; font-weight: 700; }
  .person-role { font-size: 7px; color: var(--muted); letter-spacing: 0.04em; }
  .card-white .gold-bar { right: 0; top: 21px; width: 8px; height: 21px; }
  .card-white .contact { right: 19px; text-align: right; font-size: 5.6px; }
</style>
</head>
<body>
  <div class="backdrop"></div>

  <!-- letterhead -->
  <div class="piece letterhead">
    <span class="faint-name" style="left:424px;top:632px;font-size:52px">Valtrix</span>
    <div class="wordmark"><span class="wordmark-dot"></span><span class="wordmark-name">Valtrix</span></div>
    <div class="gold-bar" style="left:0;top:691px;width:14px;height:78px"></div>
    <div class="contact" style="left:26px;top:700px">480 Harbour Lane<br>Suite 9 Northfield, BC V2K 4M8<br><span class="label">Office.</span> 1-800-555-0142<br><span class="label">fax.</span> 1-800-555-0143<br><span class="label">web.</span> www.brightwhiskerclub.com</div>
  </div>

  <!-- envelope back -->
  <div class="piece envelope-back">
    <svg class="flap" width="541" height="80" viewBox="0 0 541 80">
      <path d="M0 0 H541 L519 52 Q515 60 505 60 L272 76 L36 60 Q26 59 22 52 Z" fill="var(--card-black)"/>
    </svg>
    <div class="flap-name">Brightwhiskerclub</div>
    <div class="flap-web">www.brightwhiskerclub.com</div>
  </div>

  <!-- envelope front -->
  <div class="piece envelope-front">
    <span class="faint-name" style="left:401px;top:122px;font-size:40px">Valtrix</span>
    <div class="wordmark"><span class="wordmark-dot"></span><span class="wordmark-name">Valtrix</span></div>
    <div class="gold-bar" style="left:0;top:178px;width:8px;height:47px"></div>
    <div class="contact" style="left:21px;top:186px;font-size:7.4px">480 Harbour Lane<br>Suite 9 Northfield, BC V2K 4M8<br><span class="label">Office.</span> 1-800-555-0142<br><span class="label">fax.</span> 1-800-555-0143</div>
  </div>

  <!-- business card: brand side -->
  <div class="piece card-black">
    <div class="mascot-area" role="img" aria-label="Brightwhiskerclub brand illustration"></div>
    <div class="club-name">Brightwhiskerclub</div>
    <div class="club-web">www.brightwhiskerclub.com</div>
  </div>

  <!-- business card: contact side -->
  <div class="piece card-white">
    <div class="wordmark"><span class="wordmark-dot"></span><span class="wordmark-name">Valtrix</span></div>
    <div class="person">
      <div class="person-name">Daniel Reyes</div>
      <div class="person-role">Marketing Manager</div>
    </div>
    <div class="gold-bar"></div>
    <div class="contact" style="top:78px">480 Harbour Lane<br>Suite 9 Northfield, BC V2K 4M8</div>
    <div class="contact" style="top:105px"><span class="label">Office.</span> 1-800-555-0142<br><span class="label">Fax.</span> 1-800-555-0143<br><span class="label">Email.</span> info@brightwhiskerclub.com</div>
  </div>
</body>
</html>
```